Fornello Oak Hearth Kitchen (restaurant)

Restaurant with a cool vibe.
We need a refresh of existing site. Appealing to a hip crowd of 25 or older age bracket (mid price to high small town). Constant changes food and cocktail menu. A vibing atmosphere with jazz funk hip music.
Must be able to scale for any device… phone/mobile device super important.
Instagram: @Velmora.Brisket
Website: velmorabrisket.example

Target Market(s)

25-55 age group

Number of Pages Required

1 page

Font styles to use
Sans Serif

Requirements
Must have
• Simple to navigate. Simplicity is the key to all sophistication.

Links/Buttons
Menu
Gift Cards
Reservations
Take Out
Contact Us
Should not have
• Please, nothing generic looking… no cookie cutter look. Originality

```html
<!DOCTYPE html>
<html lang="en">
<head>
<meta charset="utf-8">
<title>Fornello Oak Hearth Kitchen</title>
<link rel="stylesheet" href="https://fonts.googleapis.com/css2?family=Poppins:ital,wght@0,400;0,500;0,600;0,700;1,400&family=Oswald:wght@300&display=swap">
<style>
:root{
  --ink:#141414;
  --yellow:#fdd32a;
  --text:#555;
  --muted:#888;
  --hero:#f1f1f1;
  --footer:#141414;
  --white:#fff;
  --line:#d9d9d9;
}
*{box-sizing:border-box;margin:0;padding:0}
html,body{width:1200px;height:2954px;overflow:hidden}
body{position:relative;background:var(--white);font-family:'Poppins',sans-serif;color:var(--ink)}
.abs{position:absolute}
.photo{position:absolute}

.topbar{left:0;top:0;width:1200px;height:39px;background:var(--ink);color:var(--white);font-size:11px;font-weight:600;text-align:center;line-height:39px;letter-spacing:.2px}

.hero{left:0;top:39px;width:1200px;height:680px;background:linear-gradient(180deg,#fbfbfb 0%,var(--hero) 55%,#fafafa 100%)}
.brand{left:88px;top:62px;font-weight:700;font-size:37px;line-height:36px;letter-spacing:2px;color:var(--ink)}
.brand small{display:block;font-size:13px;font-weight:700;letter-spacing:.3px;line-height:18px;padding-left:22px}
.nav{right:90px;top:66px;display:flex;align-items:center;gap:24px;font-size:13px;font-weight:500;text-transform:uppercase}
.nav .pill{background:#ececec;border-radius:20px;padding:12px 20px;font-weight:600}

.hero-title{left:0;width:1200px;top:216px;text-align:center;font-size:66px;font-weight:700;line-height:60px;letter-spacing:1px}
.booking{left:214px;top:372px;width:772px;height:98px;background:var(--white);border-radius:50px;box-shadow:0 12px 30px rgba(0,0,0,.08)}
.field{position:absolute;top:24px;width:132px;border-bottom:1px solid var(--line);padding-bottom:8px}
.field .label{display:flex;align-items:center;gap:5px;font-size:16px;color:#9a9a9a;margin-bottom:10px}
.field .value{font-size:12px;font-weight:500;display:flex;justify-content:space-between}
.btn-find{position:absolute;left:580px;top:31px;width:156px;height:37px;background:var(--yellow);border-radius:20px;font-size:15px;font-weight:600;text-align:center;line-height:37px}

.eyebrow{left:89px;top:922px;display:flex;align-items:center;gap:10px;font-family:'Oswald',sans-serif;font-weight:300;font-size:18px;color:var(--muted)}
.eyebrow:before{content:"";width:48px;height:2px;background:var(--yellow)}
.about-title{left:89px;top:950px;font-size:43px;font-weight:700}
.about-copy{left:89px;top:1013px;width:420px;font-size:16px;line-height:24px;color:var(--text)}

.card{position:absolute;overflow:hidden;color:var(--white);font-size:27px;font-weight:700}
.card span{position:absolute;bottom:22px;left:0;width:100%;text-align:center}
.ring{position:absolute;border:2px solid var(--ink);border-radius:50%}

.service{position:absolute;top:1402px;width:200px;text-align:center}
.service .disc{width:147px;height:147px;margin:0 auto;border-radius:50%;display:flex;align-items:center;justify-content:center}
.service p{margin-top:20px;font-size:18px;font-weight:600}
.dot{position:absolute;width:10px;height:10px;border-radius:50%;background:#ddd}

.section-title{left:0;width:1200px;text-align:center;font-size:42px;font-weight:700}
.recipe{top:1764px;width:195px;height:259px}

.quote-mark{font-family:'Poppins',sans-serif;font-size:190px;font-weight:700;color:#efefef;line-height:1}
.avatar{position:absolute;width:130px;height:130px;border-radius:50%;background:var(--white);box-shadow:0 6px 18px rgba(0,0,0,.12);padding:9px}
.avatar div{width:100%;height:100%;border-radius:50%}
.testimonial{position:absolute;top:2280px;width:345px}
.testimonial q{display:block;font-style:italic;font-size:19px;line-height:22px;color:#666;quotes:none}
.testimonial .name{margin-top:28px;font-weight:600;font-size:15px;letter-spacing:.5px}
.testimonial .role{font-size:13px;color:#666}

.footer{left:0;top:2548px;width:1200px;height:406px;background:var(--footer);color:var(--white)}
.footer .brand{color:var(--white)}
.social{position:absolute;display:flex;gap:6px}
.social i{display:block;width:26px;height:26px;border-radius:50%;background:#2c2c2c}
.col{position:absolute;font-size:13px;line-height:26px;color:#ddd}
.col h4{font-size:18px;font-weight:600;color:var(--white);margin-bottom:6px}
.contact-row{display:flex;gap:8px;align-items:flex-start}
.rule{left:94px;top:2903px;width:1020px;height:1px;background:#333}
.copyright{left:0;width:1200px;top:2920px;text-align:center;font-size:11px;font-weight:600}
.to-top{left:1142px;top:2884px;width:32px;height:32px;border-radius:50%;background:var(--yellow)}
</style>
</head>
<body>

<div class="abs topbar">RATED 5 STARS BY CUSTOMERS FOR QUALITY &amp; DELIVERY!</div>

<section class="abs hero"></section>

<div class="abs brand">FORNELLO<small>Oak Hearth Kitchen</small></div>
<nav class="abs nav">
  <span>Menu</span><span>Gift Cards</span><span>Reservations</span><span>Take Out</span><span class="pill">Contact Us</span>
</nav>

<div class="photo" role="img" aria-label="Burger with guacamole, tomato and greens" style="left:-40px;top:150px;width:330px;height:470px;border-radius:48% 52% 45% 55%;background:radial-gradient(circle at 45% 45%,#b9a23a,#8a5a2c 55%,#6f3f22)"></div>
<div class="photo" role="img" aria-label="Wood fired pizza on a blue plate" style="left:1006px;top:132px;width:240px;height:310px;border-radius:50%;background:radial-gradient(circle at 40% 50%,#e7d6b0,#c98f5a 60%,#a8c8d8 75%)"></div>
<div class="photo" role="img" aria-label="Spices and vegetables on a cutting board" style="left:1031px;top:516px;width:190px;height:212px;border-radius:40%;background:radial-gradient(circle at 50% 50%,#e0b43a,#b05a2e 55%,#5e7a3a)"></div>
<div class="photo" role="img" aria-label="Lettuce wraps with chili dip on a dark plate" style="left:399px;top:521px;width:237px;height:256px;border-radius:50%;background:radial-gradient(circle at 50% 50%,#a33a2a,#5f8a3a 45%,#262626 70%);box-shadow:0 20px 30px rgba(0,0,0,.2)"></div>

<h1 class="abs hero-title">Lets Get Lunch<br>At Fornello!</h1>

<form class="abs booking">
  <div class="field" style="left:74px">
    <div class="label"><svg width="14" height="14" viewBox="0 0 14 14" fill="none" stroke="#aaa"><rect x="1" y="2" width="12" height="11" rx="1"/><path d="M1 5h12M4 1v2M10 1v2"/></svg>Date</div>
    <div class="value">Wed, Jul 14, 2021</div>
  </div>
  <div class="field" style="left:232px">
    <div class="label"><svg width="15" height="15" viewBox="0 0 15 15" fill="none" stroke="#aaa"><circle cx="7.5" cy="7.5" r="6.5"/><path d="M7.5 4v4l-2 1.5"/></svg>Time</div>
    <div class="value">Closed<span>⌄</span></div>
  </div>
  <div class="field" style="left:390px">
    <div class="label"><svg width="15" height="15" viewBox="0 0 15 15" fill="none" stroke="#aaa"><circle cx="7.5" cy="5" r="3.5"/><path d="M1 14c1-4 12-4 13 0"/></svg>Party Size</div>
    <div class="value">04<span>⌄</span></div>
  </div>
  <div class="btn-find">FIND A TABLE</div>
</form>

<div class="abs eyebrow">OUR STORY</div>
<h2 class="abs about-title">About Fornello</h2>
<p class="abs about-copy">Aenean sollicitudin, lorem quis bibendum auctor, nisi elit consequat ipsum, nec sagittis sem nibh id elit. Duis sed odio sit amet nibh vulputate cursus a sit amet mauris morbi accumsan ipsum velit. Nam nec tellus a odio tincidunt auctor a ornare odio....</p>
<div class="photo" role="img" aria-label="Handwritten signature of the owner" style="left:89px;top:1152px;width:180px;height:46px;background:linear-gradient(90deg,#eee,#f7f7f7)"></div>

<div class="photo" role="img" aria-label="Salad bowl" style="left:-60px;top:1284px;width:165px;height:234px;border-radius:50%;background:radial-gradient(circle at 45% 50%,#c8a24a,#6e7a3a 55%,#555 80%)"></div>

<div class="abs" style="left:674px;top:928px;width:344px;height:344px;border-radius:50%;background:var(--yellow)"></div>
<div class="card" style="left:612px;top:881px;width:234px;height:346px;border-radius:0 0 28px 0;background:linear-gradient(160deg,#7a5a3a,#3a3026 60%,#1c1c1c)" role="img" aria-label="Grilled chicken dinner plate"><span>Dinner</span></div>
<div class="card" style="left:873px;top:981px;width:235px;height:346px;border-radius:0 0 28px 0;background:linear-gradient(160deg,#b58a5a,#5b4a6a 50%,#2a2a2a)" role="img" aria-label="Street tacos with red cabbage"><span>Takeout</span></div>
<div class="ring" style="left:876px;top:902px;width:57px;height:57px"></div>
<div class="ring" style="left:800px;top:1245px;width:37px;height:37px"></div>

<div class="service" style="left:229px">
  <div class="disc" style="background:var(--ink)">
    <svg width="70" height="80" viewBox="0 0 70 80" fill="none" stroke="#fff" stroke-width="3"><rect x="18" y="4" width="34" height="62" rx="5"/><path d="M28 28h14l-2 14H30z" stroke="#fdd32a"/><path d="M31 28v-4a4 4 0 0 1 8 0v4" stroke="#fdd32a"/><path d="M18 50c-8 2-12 10-8 22h20"/><circle cx="58" cy="30" r="4"/><circle cx="58" cy="44" r="4"/></svg>
  </div>
  <p>Order Online</p>
</div>
<div class="dot" style="left:439px;top:1462px"></div><div class="dot" style="left:458px;top:1478px"></div><div class="dot" style="left:481px;top:1478px"></div>
<div class="service" style="left:500px">
  <div class="disc" style="background:var(--yellow)">
    <svg width="80" height="70" viewBox="0 0 80 70" fill="none" stroke="#141414" stroke-width="3"><circle cx="14" cy="10" r="5"/><circle cx="66" cy="10" r="5"/><path d="M6 20v40M74 20v40M6 40h16v20M74 40H58v20M20 30h40v8c-4 4-4 20 0 24H20c4-4 4-20 0-24z"/></svg>
  </div>
  <p>Book A Table</p>
</div>
<div class="dot" style="left:710px;top:1478px"></div><div class="dot" style="left:728px;top:1462px"></div><div class="dot" style="left:752px;top:1462px"></div>
<div class="service" style="left:771px">
  <div class="disc" style="background:var(--ink)">
    <svg width="84" height="84" viewBox="0 0 84 84" fill="none" stroke="#fff" stroke-width="3"><path d="M74 34A34 34 0 1 0 42 76"/><path d="M68 26l6 8 6-8"/><path d="M26 40l10 8 16-20" stroke="#fdd32a"/><text x="44" y="78" fill="#fff" stroke="none" font-family="Poppins,sans-serif" font-size="30">24</text></svg>
  </div>
  <p>Hours Contact</p>
</div>

<h2 class="abs section-title" style="top:1682px">Browse the recipes</h2>
<div class="photo recipe" style="left:87px;background:linear-gradient(150deg,#c98a3a,#7a4a6a 50%,#3a2a1e)" role="img" aria-label="Taco close-up"></div>
<div class="photo recipe" style="left:294px;background:linear-gradient(150deg,#e6d8b8,#c48a4a 50%,#7a4a2a)" role="img" aria-label="Flatbread pizza on wooden board"></div>
<div class="photo recipe" style="left:501px;background:linear-gradient(150deg,#8a8a80,#b89a5a 50%,#6a5a3a)" role="img" aria-label="Tacos with lime on a metal tray"></div>
<div class="photo recipe" style="left:707px;background:linear-gradient(150deg,#3a4a4a,#8a8a4a 45%,#b0764a)" role="img" aria-label="Bowls of hummus and dips"></div>
<div class="photo recipe" style="left:914px;background:linear-gradient(150deg,#c8b08a,#7a5a8a 50%,#4a3a2a)" role="img" aria-label="Plated tacos with cabbage"></div>

<h2 class="abs section-title" style="top:2122px">Testimonials</h2>
<div class="abs quote-mark" style="left:396px;top:2170px">“</div>
<div class="abs quote-mark" style="left:933px;top:2170px">“</div>

<div class="avatar" style="left:93px;top:2268px"><div role="img" aria-label="Customer portrait" style="background:linear-gradient(160deg,#b8b8b8,#6a6a6a)"></div></div>
<div class="testimonial" style="left:237px">
  <q>Duis sed odio sit amet nibh vulputate cursus a sit amet mauris. Morbi accumsan ipsum velit. Nam nec tellus a odio tincidunt auctor...</q>
  <div class="name">-DANA L. WHITFORD /</div>
  <div class="role">CEO</div>
</div>
<div class="avatar" style="left:629px;top:2268px"><div role="img" aria-label="Customer portrait" style="background:linear-gradient(160deg,#d8c2a8,#8a6a5a)"></div></div>
<div class="testimonial" style="left:773px">
  <q>Duis sed odio sit amet nibh vulputate cursus a sit amet mauris. Morbi accumsan ipsum velit. Nam nec tellus a odio tincidunt auctor...</q>
  <div class="name">-DANA L. WHITFORD /</div>
  <div class="role">CEO</div>
</div>

<footer class="abs footer"></footer>
<div class="photo" role="img" aria-label="Bowl of hummus" style="left:1054px;top:2430px;width:240px;height:240px;border-radius:50%;background:radial-gradient(circle,#c8884a,#8a5a2a 55%,#9aa6aa 72%);box-shadow:0 10px 24px rgba(0,0,0,.2)"></div>
<div class="photo" role="img" aria-label="Pizza" style="left:-90px;top:2527px;width:179px;height:179px;border-radius:50%;background:radial-gradient(circle,#e2b66a,#b05a2a 70%,#2a2a2a 80%)"></div>

<div class="abs brand" style="left:147px;top:2706px;color:var(--white)">FORNELLO<small>Oak Hearth Kitchen</small></div>
<div class="social" style="left:174px;top:2772px" aria-label="Social links"><i></i><i></i><i></i><i></i></div>

<div class="col" style="left:400px;top:2652px">
  <h4>Useful Links</h4>
  Menu<br>Gift Cards<br>Reservations<br>Take Out<br>Contact Us
</div>
<div class="col" style="left:593px;top:2652px">
  <h4>Dining Hours</h4>
  Courtyard is open<br>Thursday to Sunday<br>12:00pm – 9:00pm
  <h4 style="margin-top:14px">Pickup &amp; Kitchen Hours</h4>
  Thursday to Sunday<br>12:00pm – 8:00pm
</div>
<div class="photo" role="img" aria-label="Faint dotted world map" style="left:890px;top:2710px;width:160px;height:105px;background:radial-gradient(ellipse,#2a2a2a,transparent 70%)"></div>
<div class="col" style="left:864px;top:2652px">
  <h4>Get In Touch</h4>
  <div class="contact-row" style="line-height:18px;margin-top:4px"><svg width="10" height="14" viewBox="0 0 10 14"><path d="M5 0a5 5 0 0 1 5 5c0 4-5 9-5 9S0 9 0 5a5 5 0 0 1 5-5z" fill="#fdd32a"/><circle cx="5" cy="5" r="2" fill="#141414"/></svg><span>48 Marlow Lane<br>Brookfield, ON</span></div>
  <div class="contact-row"><svg width="11" height="11" viewBox="0 0 12 12" style="margin-top:7px"><path d="M2 0l3 3-1.5 2a7 7 0 0 0 3.5 3.5L9 7l3 3-2 2C5 12 0 7 0 2z" fill="#fdd32a"/></svg><span>555-014-2290</span></div>
  <div class="contact-row"><svg width="12" height="9" viewBox="0 0 12 9" style="margin-top:8px"><rect width="12" height="9" fill="#fdd32a"/><path d="M0 0l6 5 6-5" stroke="#141414" fill="none"/></svg><span>hello@velmorabrisket.example</span></div>
</div>

<div class="abs rule"></div>
<div class="abs copyright" style="color:var(--white)">COPYRIGHT © 2021 FORNELLO ALL RIGHTS RSERVED</div>
<div class="abs to-top"><svg width="32" height="32" viewBox="0 0 32 32"><path d="M13 18l3-3 3 3" stroke="#141414" stroke-width="1.5" fill="none"/></svg></div>

</body>
</html>
```